Visual design for database driven web application

Need a clean, professional looking visual design for a web application.

PLUMB is the new standardized K-12 school testing program for the state of Texas. We are building an application named PLUMB-Finder (clever, yeah?) that will allow teachers, school administrators, and others to EASILY sort through millions of records of student data and print or export reports showing just the information they need about their students.

The state currently doesn't provide a user-friendly way to do this. They provide a "data dump" spreadsheet that school administrators and teachers must figure out how to manipulate to get the data they need. We are building a Web-based tool that will make it super simple and easy for our users to get the data they need in a format that works for them.

I've created a basic wireframe of the main application screen in Wirella Kit Plus. I need you to "skin" the wireframe to make it look good. Your mockup will set the tone for branding and visual design throughout the site.

See the attached screenshots. There are a few variations of the screen that include dynamic panels that open & close. Start by designing just the main screen and if you have time, do one or two of the panels. Thanks!
Updates

Target Market(s)

K-12 education professionals (teachers, administrators) in the state of Texas

Industry/Entity Type

Building

Requirements
Must have
• Your mockups should include all of the features & content shown in the attached screenshots.

However, you don't have to show all 10 rows of data. You can just do the column headers and one row of data. (It would be repetitive and unnecessary to spend time re-creating the entire grid with all of that data just to show your visual styling.)

The design should reflect the following concepts:

- Texas
- Education
- Simplicity
- Helpfulness
- Trust
- Professionalism

If I select your design, I will want your design source files (Illustrator, Photoshop, etc.)
Nice to have
• A logo in the upper left corner for PLUMB-Finder. The logo should definitely communicate the design concepts described under "must have."

```html
<!DOCTYPE html>
<html lang="en">
<head>
<meta charset="utf-8">
<title>PLUMB-Finder · Student Data</title>
<link rel="stylesheet" href="https://fonts.googleapis.com/css2?family=Questrial&display=swap">
<style>
:root{
  --ink:#2b2b2b;
  --navy:#1c4f80;
  --link:#0f5c9e;
  --blue:#2f9be3;
  --blue-dark:#1771c4;
  --page-active:#1b5c93;
  --row-a:#f3f3f3;
  --row-b:#e4e4e4;
  --rule:#cfcfcf;
  --header-top:#f7f7f7;
  --header-bot:#dcdcdc;
  --disc:#2a2a2a;
}
*{box-sizing:border-box;margin:0;padding:0}
html,body{width:1200px;height:885px;overflow:hidden}
body{position:relative;font-family:"Questrial",sans-serif;color:var(--ink);background:#fff;font-size:13px}
.masthead{position:absolute;left:0;top:0;width:1200px;height:157px;
  background:linear-gradient(180deg,var(--header-top) 0%,#ebebeb 60%,var(--header-bot) 100%);overflow:hidden}
.masthead .swoosh{position:absolute;left:0;top:0}
.brand{position:absolute;left:40px;top:44px;display:flex;align-items:center;gap:18px}
.brand-mark{width:70px;height:44px;background:var(--blue-dark)}
.brand-name{font-size:38px;color:var(--blue-dark);letter-spacing:0.5px;margin-left:16px}
.welcome{position:absolute;left:612px;top:56px;font-size:19px;color:#333}
.user-links{position:absolute;top:37px;font-size:13px;color:var(--navy);display:flex;align-items:center;gap:8px}
.user-links .dot{width:18px;height:18px;border-radius:50%;background:#c4572b}
.user-links .sq{width:22px;height:20px;background:#8a7a4a}
.search-field{position:absolute;left:905px;top:72px;width:187px;height:30px;background:#fff;border-radius:5px;box-shadow:inset 0 1px 3px rgba(0,0,0,.2)}
.search-field svg{position:absolute;right:8px;top:3px}
.search-btn{position:absolute;left:1105px;top:72px;width:78px;height:30px;border-radius:4px;
  background:linear-gradient(180deg,#4fb3f3,var(--blue-dark));color:#fff;font-size:13px;text-align:center;line-height:30px}
.search-options{position:absolute;left:1084px;top:126px;color:var(--navy);font-size:13px}
.tab{position:absolute;top:118px;height:39px;width:153px;border-radius:5px 5px 0 0;color:#fff;font-size:15px;text-align:center;line-height:45px}
.tab-instructions{left:14px;background:linear-gradient(180deg,#49b0f2,#1f7fcc)}
.tab-data{left:175px;background:linear-gradient(180deg,#2a7fc0,#0e4f86)}
.toolbar{position:absolute;left:0;top:157px;width:1200px;height:70px;background:linear-gradient(180deg,#fff,#f2f2f2);font-size:13px;color:var(--navy)}
.toolbar span{position:absolute;top:27px}
.pager{position:absolute;left:12px;display:flex;align-items:center;font-size:13px;color:#333}
.pager .disc{width:25px;height:25px;border-radius:50%;background:var(--disc);display:flex;align-items:center;justify-content:center}
.pager .page{width:18px;height:18px;background:var(--blue);color:#fff;font-size:12px;text-align:center;line-height:18px;margin-right:6px}
.pager .page.current{background:var(--page-active)}
.pager .select{width:50px;height:20px;border:1px solid #888;border-radius:4px;background:linear-gradient(#fff,#ddd);font-size:12px;padding-left:10px;line-height:18px;position:relative}
.pager .select i{position:absolute;right:3px;top:2px;width:13px;height:14px;background:#7ab4e4;border-radius:2px}
.grid{position:absolute;left:0;top:290px;width:1200px;border-collapse:collapse;table-layout:fixed}
.grid th{height:48px;background:#fff;color:var(--link);font-weight:normal;font-size:15px;text-align:left;padding-left:15px;border-right:1px solid var(--rule)}
.grid td{height:45px;font-size:12.5px;color:#333;border-right:1px solid var(--rule);text-align:center}
.grid td.l{text-align:left;padding-left:6px}
.grid tbody tr:nth-child(odd){background:var(--row-a)}
.grid tbody tr:nth-child(even){background:var(--row-b)}
.grid th:last-child,.grid td:last-child{border-right:0}
.footer-band{position:absolute;left:0;top:788px;width:1200px;height:97px;background:linear-gradient(180deg,#fff,#e9e9e9)}
</style>
</head>
<body>
<header class="masthead">
  <svg class="swoosh" width="1200" height="157" viewBox="0 0 1200 157" aria-hidden="true">
    <path d="M420 0 C600 80 900 110 1200 40 L1200 0 Z" fill="#fff" opacity=".55"/>
    <path d="M520 0 C700 60 950 70 1200 10" fill="none" stroke="#fff" stroke-width="2" opacity=".8"/>
    <path d="M0 150 C200 120 300 60 420 0" fill="none" stroke="#fff" stroke-width="3" opacity=".7"/>
  </svg>
  <div class="brand"><div class="brand-mark"></div><div class="brand-name">PLUMB-FINDER</div></div>
  <div class="welcome">Welcome, Jack</div>
  <div class="user-links" style="left:972px"><span class="dot"></span>My Profile</div>
  <div class="user-links" style="left:1100px"><span class="sq"></span>Logout</div>
  <div class="search-field">
    <svg width="26" height="26" viewBox="0 0 26 26" aria-hidden="true"><circle cx="10" cy="10" r="7" fill="#bfe0f7" stroke="#2b6aa3" stroke-width="2"/><line x1="15" y1="15" x2="23" y2="23" stroke="#333" stroke-width="4" stroke-linecap="round"/></svg>
  </div>
  <div class="search-btn">Search</div>
  <div class="search-options">Search Options ›</div>
  <div class="tab tab-instructions">Instructions</div>
  <div class="tab tab-data">Student Data</div>
</header>

<section class="toolbar">
  <span style="left:23px">Showing 26 of 38 columns</span>
  <span style="left:255px">Show / Hide Columns &nbsp;‹</span>
  <span style="left:468px;color:#333">3 columns are filtered</span>
  <span style="left:1059px">Print &nbsp;&nbsp;&nbsp;|&nbsp;&nbsp;&nbsp; Download</span>
</section>

<nav class="pager" style="top:236px">
  <span class="disc"><svg width="15" height="12" viewBox="0 0 15 12"><path d="M14 6H4M7 1L2 6l5 5" stroke="#fff" stroke-width="2.5" fill="none"/></svg></span>
  <span style="margin:0 28px 0 8px">Previous</span>
  <span class="page current">1</span><span class="page">2</span><span class="page">3</span><span class="page">4</span><span class="page">5.</span>
  <span class="page" style="margin-left:34px;width:20px">50</span>
  <span style="margin:0 14px 0 38px">Next</span>
  <span class="disc"><svg width="15" height="12" viewBox="0 0 15 12"><path d="M1 6h10M8 1l5 5-5 5" stroke="#fff" stroke-width="2.5" fill="none"/></svg></span>
  <span style="margin:0 12px 0 36px">Show</span>
  <span class="select">10<i></i></span>
  <span style="margin-left:28px">rows per page</span>
</nav>

<table class="grid">
  <colgroup><col style="width:75px"><col style="width:82px"><col style="width:66px"><col style="width:85px"><col style="width:106px"><col style="width:96px"><col style="width:110px"><col style="width:110px"><col style="width:51px"><col style="width:112px"><col style="width:67px"><col style="width:110px"><col style="width:130px"></colgroup>
  <thead><tr><th>Date</th><th>Grade</th><th>ESC</th><th>CDC #</th><th>District</th><th>Campus</th><th>Last Name</th><th>Fisrt Name</th><th>MI</th><th>Student ID</th><th>Gender</th><th>DOB</th><th>Hisp</th></tr></thead>
  <tbody>
    <tr><td class="l" style="padding-left:15px">411</td><td>9</td><td>10</td><td>999999001</td><td>Example District</td><td class="l">Example HS</td><td class="l">Accountability</td><td>Nathalie</td><td></td><td class="l">630543340</td><td>F</td><td>7311996</td><td>1</td></tr>
    <tr><td class="l" style="padding-left:15px">411</td><td>9</td><td>10</td><td>999999001</td><td>Example District</td><td class="l">Example HS</td><td class="l">Accountability</td><td>Sharp</td><td class="l">I</td><td class="l">630543340</td><td>M</td><td>7311996</td><td>1</td></tr>
    <tr><td class="l" style="padding-left:15px">411</td><td>9</td><td>10</td><td>999999001</td><td>Example District</td><td class="l">Example HS</td><td class="l">Accountability</td><td>Nathalie</td><td class="l">E</td><td class="l">630543340</td><td>F</td><td>7311996</td><td>0</td></tr>
    <tr><td class="l" style="padding-left:15px">411</td><td>9</td><td>10</td><td>999999001</td><td>Example District</td><td class="l">Example HS</td><td class="l">Accountability</td><td>Sharp</td><td></td><td class="l">630543340</td><td>M</td><td>7311996</td><td>1</td></tr>
    <tr><td class="l" style="padding-left:15px">411</td><td>9</td><td>10</td><td>999999001</td><td>Example District</td><td class="l">Example HS</td><td class="l">Accountability</td><td>Nathalie</td><td class="l">B</td><td class="l">630543340</td><td>F</td><td>7311996</td><td>1</td></tr>
    <tr><td class="l" style="padding-left:15px">411</td><td>9</td><td>10</td><td>999999001</td><td>Example District</td><td class="l">Example HS</td><td class="l">Accountability</td><td>Sharp</td><td class="l">W</td><td class="l">630543340</td><td>M</td><td>7311996</td><td>0</td></tr>
    <tr><td class="l" style="padding-left:15px">411</td><td>9</td><td>10</td><td>999999001</td><td>Example District</td><td class="l">Example HS</td><td class="l">Accountability</td><td>Nathalie</td><td></td><td class="l">630543340</td><td>F</td><td>7311996</td><td>0</td></tr>
    <tr><td class="l" style="padding-left:15px">411</td><td>9</td><td>10</td><td>999999001</td><td>Example District</td><td class="l">Example HS</td><td class="l">Accountability</td><td>Sharp</td><td></td><td class="l">630543340</td><td>M</td><td>7311996</td><td>1</td></tr>
    <tr><td class="l" style="padding-left:15px">411</td><td>9</td><td>10</td><td>999999001</td><td>Example District</td><td class="l">Example HS</td><td class="l">Accountability</td><td>Nathalie</td><td class="l">J</td><td class="l">630543340</td><td>F</td><td>7311996</td><td>1</td></tr>
    <tr><td class="l" style="padding-left:15px">411</td><td>9</td><td>10</td><td>999999001</td><td>Example District</td><td class="l">Example HS</td><td class="l">Accountability</td><td>Sharp</td><td></td><td class="l">630543340</td><td>M</td><td>7311996</td><td>1</td></tr>
  </tbody>
</table>

<div class="footer-band"></div>
<nav class="pager" style="top:817px;left:41px">
  <span class="disc"><svg width="15" height="12" viewBox="0 0 15 12"><path d="M14 6H4M7 1L2 6l5 5" stroke="#fff" stroke-width="2.5" fill="none"/></svg></span>
  <span style="margin:0 28px 0 8px">Previous</span>
  <span class="page current">1</span><span class="page">2</span><span class="page">3</span><span class="page">4</span><span class="page">5.</span>
  <span class="page" style="margin-left:34px;width:20px">50</span>
  <span style="margin:0 14px 0 38px">Next</span>
  <span class="disc"><svg width="15" height="12" viewBox="0 0 15 12"><path d="M1 6h10M8 1l5 5-5 5" stroke="#fff" stroke-width="2.5" fill="none"/></svg></span>
  <span style="margin:0 12px 0 36px">Show</span>
  <span class="select">10<i></i></span>
  <span style="margin-left:28px">rows per page</span>
</nav>
</body>
</html>
```